Dr. Marissa Tevlin Medical/Chiropractic Business Card

Dr. Tevlin is a chiropractor and will require a business card that she uses every single day to book appointments on the back side of the card. Currently the office name goes by Dr. Marissa Tevlin. The chiropractic profession is based on the diagnosis and manipulative treatment of misalignments of the joints, especially those of the spinal column, which are held to cause other disorders by affecting the nerves, muscles, and organs. Dr. Marissa Tevlin is looking for a contemporary and minimalistic design.

Industry/Entity Type

Medical

Contact Information for Business Card

Name: Dr. Marissa Tevlin; Address: 748 Harcastle Rd South, London, ON N5R 2K7; Phone Number: 519.274.6193; Fax: 519.281.5046; email: marissa.tevlin@quorvamail.com

Requirements
Must have
• ability to write multiple appointments date/time on the back of card

```html
<!DOCTYPE html>
<html lang="en">
<head>
<meta charset="UTF-8">
<title>Dr. Marissa Tevlin – Business Card</title>
<link href="https://fonts.googleapis.com/css2?family=Montserrat:wght@500;600&family=Open+Sans:wght@400;600&display=swap" rel="stylesheet">
<style>
  :root {
    --navy-deep: #120d3a;
    --navy: #2a2160;
    --paper: #ffffff;
    --paper-shade: #ececec;
    --bone: #e9e9ec;
    --pain-red: #8e1e3c;
    --rule: #3a3a44;
    --stage: #d6d6d6;
  }
  * { box-sizing: border-box; margin: 0; padding: 0; }
  html, body { width: 1200px; height: 900px; overflow: hidden; }
  body {
    background: var(--stage);
    font-family: "Open Sans", sans-serif;
    position: relative;
  }
  .card {
    position: absolute;
    left: 300px;
    width: 600px;
    height: 345px;
    overflow: hidden;
    box-shadow: 0 4px 14px rgba(0,0,0,0.25);
  }
  /* ---------- Front ---------- */
  .card-front { top: 60px; background: var(--paper); }
  .front-field {
    position: absolute; inset: 0;
    width: 100%; height: 100%;
  }
  .doctor-name {
    position: absolute;
    left: 40px; top: 82px;
    font-family: "Montserrat", sans-serif;
    font-weight: 600;
    font-size: 35px;
    letter-spacing: 0.5px;
    color: var(--paper);
  }
  .contact-list {
    position: absolute;
    left: 42px; top: 155px;
    list-style: none;
    color: var(--paper);
    font-size: 15px;
    line-height: 23px;
  }
  .contact-list li { display: flex; align-items: center; gap: 8px; }
  .contact-list svg { width: 14px; height: 14px; fill: var(--paper); flex: none; }
  .address {
    position: absolute;
    left: 42px; top: 234px;
    color: var(--paper);
    font-size: 15px;
    line-height: 23px;
    font-style: normal;
  }
  /* ---------- Back ---------- */
  .card-back { top: 475px; background: linear-gradient(135deg, var(--paper) 40%, var(--paper-shade)); }
  .appointments-title {
    position: absolute;
    left: 30px; top: 22px;
    font-family: "Montserrat", sans-serif;
    font-weight: 500;
    font-size: 27px;
    letter-spacing: 1px;
    color: #111;
  }
  .column-label {
    position: absolute;
    top: 60px;
    font-size: 12px;
    letter-spacing: 1px;
    color: #222;
  }
  .label-date { left: 34px; }
  .label-time { left: 330px; }
  .appointment-rows {
    position: absolute;
    left: 30px; top: 82px;
    width: 540px;
  }
  .appointment-row {
    display: grid;
    grid-template-columns: 280px 240px;
    column-gap: 20px;
    height: 21px;
  }
  .appointment-row span { border-bottom: 1px solid var(--rule); }
  .back-band { position: absolute; left: 0; bottom: 0; width: 600px; height: 90px; }
  .reschedule-note {
    position: absolute;
    left: 0; bottom: 14px; width: 600px;
    text-align: center;
    color: var(--paper);
    font-size: 15px;
    line-height: 20px;
  }
</style>
</head>
<body>

<section class="card card-front">
  <svg class="front-field" viewBox="0 0 600 345" aria-hidden="false">
    <defs>
      <linearGradient id="navyFade" x1="0" y1="0" x2="1" y2="0">
        <stop offset="0" stop-color="#2c2462"/>
        <stop offset="1" stop-color="#0f0a33"/>
      </linearGradient>
      <linearGradient id="boneFade" x1="0" y1="0" x2="1" y2="0">
        <stop offset="0" stop-color="#e9e9ec" stop-opacity="0"/>
        <stop offset="0.3" stop-color="#e9e9ec"/>
        <stop offset="0.75" stop-color="#e9e9ec"/>
        <stop offset="1" stop-color="#e9e9ec" stop-opacity="0"/>
      </linearGradient>
      <radialGradient id="painGlow" cx="0.5" cy="0.5" r="0.5">
        <stop offset="0" stop-color="#8e1e3c" stop-opacity="0.95"/>
        <stop offset="0.55" stop-color="#8e1e3c" stop-opacity="0.6"/>
        <stop offset="1" stop-color="#8e1e3c" stop-opacity="0"/>
      </radialGradient>
      <clipPath id="navyShape">
        <path d="M0 0 H600 V335 Q300 275 0 315 Z"/>
      </clipPath>
    </defs>
    <path d="M0 0 H600 V335 Q300 275 0 315 Z" fill="url(#navyFade)"/>
    <g class="spine-visual" role="img" aria-label="Illustration of a spinal column with a red glow marking an area of pain" clip-path="url(#navyShape)">
      <rect x="455" y="0" width="110" height="345" fill="url(#boneFade)"/>
      <circle cx="500" cy="170" r="85" fill="url(#painGlow)"/>
    </g>
  </svg>

  <h1 class="doctor-name">DR. MARISSA TEVLIN</h1>
  <ul class="contact-list">
    <li>
      <svg viewBox="0 0 24 24"><path d="M6.6 10.8a15.1 15.1 0 0 0 6.6 6.6l2.2-2.2a1 1 0 0 1 1-.25 11.4 11.4 0 0 0 3.6.57 1 1 0 0 1 1 1V20a1 1 0 0 1-1 1A17 17 0 0 1 3 4a1 1 0 0 1 1-1h3.5a1 1 0 0 1 1 1c0 1.25.2 2.45.57 3.570a1 1 0 0 1-.25 1z"/></svg>
      519.274.6193
    </li>
    <li>
      <svg viewBox="0 0 24 24"><path d="M6 2h12v6H6zM4 9h16a2 2 0 0 1 2 2v6h-4v5H6v-5H2v-6a2 2 0 0 1 2-2zm4 8v3h8v-5H8z"/></svg>
      519.281.5046
    </li>
    <li>
      <svg viewBox="0 0 24 24"><path d="M2 5h20v14H2zm2 2v.4l8 5.3 8-5.3V7zm0 2.8V17h16V9.8l-8 5.3z"/></svg>
      marissa.tevlin@quorvamail.com
    </li>
  </ul>
  <address class="address">748 Harcastle Rd South,<br>London, ON N5R 2K7</address>
</section>

<section class="card card-back">
  <h2 class="appointments-title">APPOINTMENTS</h2>
  <span class="column-label label-date">DATE</span>
  <span class="column-label label-time">TIME</span>
  <div class="appointment-rows">
    <div class="appointment-row"><span></span><span></span></div>
    <div class="appointment-row"><span></span><span></span></div>
    <div class="appointment-row"><span></span><span></span></div>
    <div class="appointment-row"><span></span><span></span></div>
    <div class="appointment-row"><span></span><span></span></div>
    <div class="appointment-row"><span></span><span></span></div>
    <div class="appointment-row"><span></span><span></span></div>
    <div class="appointment-row"><span></span><span></span></div>
  </div>
  <svg class="back-band" viewBox="0 0 600 90" preserveAspectRatio="none" aria-hidden="true">
    <path d="M0 40 Q300 0 600 25 V90 H0 Z" fill="var(--navy-deep)"/>
  </svg>
  <p class="reschedule-note">If you are unable to make your appointment,<br>please call us to reschedule</p>
</section>

</body>
</html>
```